CRM Application Interface Design

We have a wireframe / design draft for a CRM application (similar to Quillmarket, Kavu, etc.). We need this draft to be restyled to create a more finished, polished application user interface. There is a specific branding color scheme that must be adhered to, but you may add secondary and tertiary colors as needed.
At a minimum, these branding colors are required to appear in the design:
#CC0000 : Primary brand color
#AA0000 : Primary shaded (e.g. hover) color
#DBEEF5 / #4A4A4A : Gray
Some other colors you may wish to add:
* "Error/warning" color of your choice
* "Informational / focus" color of your choice
Two screens are provided, both should be re-styled as you see fit in order to finish the design:
1. "Search for customers" screen
2. "View customer details" screen
Requirements:
1. Must have the navigation along the top, cannot switch to a left nav. Must also remain two-level navigation (primary nav at top with sub nav beneath it).
2. The design must use the primary red color in a thoughtful, balanced way, without overdoing it. Please make use of other colors if needed to offset the use of red.
3. Text must be high enough contrast to be readable. The wireframe/draft screens attached show a "washed-out" low-contrast UI with light gray text. That design theme should not be used in the final design.
Aside from the above requirements, please feel free to think creatively and present substantially different ideas. Some of the things we are open to changing include:
* Element style (eg. square vs. rounded corners, flat vs. depth)
* Use of color vs. grayscale
* Menus and navigation
* Light / dark theme
* Any other stylistic elements
* Minor layout changes can be made if needed, but elements should not be moved if that can be avoided.
Goals:
* This is a business application that is used frequently and for long periods, so should not have any unnecessary distracting elements.
* Looking for a design that is clean, professional, readable, usable, and intuitive.

```html
<!DOCTYPE html>
<html lang="en">
<head>
<meta charset="utf-8">
<title>Customer Profile – Meridian CRM</title>
<link href="https://fonts.googleapis.com/css2?family=Open+Sans:wght@400;600;700&display=swap" rel="stylesheet">
<style>
:root{
  --brand:#CC0000;
  --brand-dark:#AA0000;
  --ink:#333333;
  --ink-soft:#555555;
  --slate:#4A4A4A;
  --slate-light:#666666;
  --row-line:#5a5a5a;
  --sky:#E8F3F8;
  --band:#EEEEEE;
  --line:#D9D9D9;
  --star:#F5C518;
  --white:#FFFFFF;
}
*{box-sizing:border-box;margin:0;padding:0}
html,body{width:1200px;height:902px;overflow:hidden;background:var(--white);font-family:"Open Sans",sans-serif;color:var(--ink)}
.app{position:relative;width:1200px;height:902px}
.abs{position:absolute}

/* header */
.topbar{position:absolute;left:0;top:0;width:1200px;height:83px}
.brand-name{position:absolute;left:125px;top:28px;display:flex;align-items:center;gap:8px;font-size:18px;font-weight:700;color:var(--ink)}
.brand-name .dot{width:14px;height:14px;background:var(--brand)}
.primary-nav{position:absolute;left:286px;top:31px;display:flex;font-size:13.5px;color:var(--ink)}
.primary-nav a{text-decoration:none;color:inherit;padding:0 19px;border-left:1px solid var(--ink);line-height:18px}
.primary-nav a:first-child{border-left:none;padding-left:0}
.primary-nav a.active{color:var(--brand)}
.active-marker{position:absolute;left:420px;top:0;width:30px;height:18px;background:var(--brand)}
.util{position:absolute;top:31px;display:flex;align-items:center;gap:6px;font-size:13.5px;line-height:18px}
.avatar{position:absolute;left:1021px;top:25px;width:30px;height:30px}

/* sub nav */
.subnav{position:absolute;left:0;top:83px;width:1200px;height:44px;background:var(--band);font-size:13.5px}
.subnav span{position:absolute;top:13px}
.subnav .current{left:371px;top:0;width:116px;height:44px;background:var(--brand);color:var(--white);text-align:center;line-height:44px}
.crumbs{position:absolute;left:0;top:127px;width:1200px;height:43px;background:var(--sky);font-size:13.5px;display:flex;align-items:center;padding-left:125px;gap:14px}
.crumbs .sep{width:8px;height:8px;background:var(--brand)}

/* record nav */
.back{position:absolute;left:125px;top:205px;font-size:13px;display:flex;align-items:center;gap:6px}
.pager{position:absolute;top:203px;width:22px;height:22px;border:1px solid var(--ink);display:flex;align-items:center;justify-content:center}

/* customer card */
.card{position:absolute;left:125px;top:247px;width:298px;height:606px;border-top:3px solid var(--brand);border-bottom:4px solid var(--brand);background:var(--slate);color:var(--white)}
.photo{position:absolute;left:25px;top:25px;width:105px;height:105px;border:2px solid var(--white);background:linear-gradient(160deg,#8a8f96,#4d5a6b)}
.card-name{position:absolute;left:148px;top:34px;width:124px;text-align:center;font-size:17.5px;line-height:22px}
.send{position:absolute;left:157px;top:86px;width:108px;height:30px;background:var(--brand);border:1px solid var(--white);font-size:11.5px;font-weight:600;display:flex;align-items:center;justify-content:center;gap:8px}
.facts{position:absolute;left:0;top:155px;width:298px;list-style:none;background:var(--slate-light)}
.facts li{height:36.7px;border-bottom:1px solid var(--row-line);display:flex;align-items:center;font-size:13px}
.facts .k{width:155px;padding-left:24px}
.stars{display:flex;gap:3px}
.updated{position:absolute;left:0;top:521px;width:298px;padding:12px 0 0 24px;font-size:13px;line-height:18.5px;display:flex}
.updated .k{width:155px}

/* tabs */
.tabs{position:absolute;left:450px;top:203px;height:44px;display:flex;gap:4px}
.tab{height:44px;background:var(--band);display:flex;align-items:center;justify-content:center;gap:8px;font-size:13px;color:var(--ink-soft)}
.tab.active{background:var(--brand);color:var(--white)}
.tab-line{position:absolute;left:450px;top:247px;width:625px;height:3px;background:var(--brand)}
.panel{position:absolute;left:450px;top:250px;width:625px;height:606px;border:1px solid var(--line);border-top:none}
.sections{position:absolute;left:465px;top:280px;list-style:none;font-size:12.5px;color:var(--ink-soft)}
.sections li{height:37px}
.sections li.active{color:var(--brand)}
.sections li.active::before{content:"›";margin-right:7px}

/* form */
.form{position:absolute;left:625px;top:284px;width:401px;height:523px;border:1px solid var(--line);padding:23px 0 0 26px;display:grid;grid-template-columns:177px 177px;column-gap:20px;grid-auto-rows:82.5px;font-size:11px}
.field label{display:block;margin-bottom:6px;color:var(--ink)}
.input{height:37px;border:1px solid var(--line);padding:0 15px;display:flex;align-items:center;justify-content:space-between;font-size:11px}
.seg{display:flex;height:37px;border:1px solid var(--line)}
.seg span{flex:1;display:flex;align-items:center;justify-content:center}
.seg .on{background:var(--slate);color:var(--white)}
.scroll{position:absolute;left:1061px;top:284px;width:3px;height:523px;background:#e4e4e4}
.scroll i{position:absolute;left:0;top:224px;width:3px;height:75px;background:var(--brand)}
.save{position:absolute;left:943px;top:817px;width:106px;height:30px;background:var(--brand);color:var(--white);font-size:11.5px;font-weight:600;display:flex;align-items:center;justify-content:center;gap:8px}
</style>
</head>
<body>
<div class="app">

  <header class="topbar">
    <div class="brand-name"><span class="dot"></span>Meridian</div>
    <span class="active-marker"></span>
    <nav class="primary-nav">
      <a href="#">Dashboard</a><a href="#" class="active">Customers</a><a href="#">Admin</a><a href="#">Sales</a><a href="#">Settings</a>
    </nav>
    <div class="util" style="left:771px">
      <svg width="10" height="12" viewBox="0 0 10 12"><path d="M5 0a4 4 0 0 0-4 4c0 3 4 8 4 8s4-5 4-8a4 4 0 0 0-4-4z" fill="#CC0000"/><circle cx="5" cy="4" r="1.5" fill="#fff"/></svg>
      Locations
      <svg width="10" height="6" viewBox="0 0 10 6"><path d="M1 1l4 4 4-4" stroke="#333" fill="none" stroke-width="1.3"/></svg>
    </div>
    <div class="util" style="left:892px">
      <svg width="11" height="11" viewBox="0 0 10 10"><path d="M5 0l1.5 3.3 3.5.4-2.6 2.4.7 3.5L5 7.8 1.9 9.6l.7-3.5L0 3.7l3.5-.4z" fill="#CC0000"/></svg>
      Favourites
      <svg width="10" height="6" viewBox="0 0 10 6"><path d="M1 1l4 4 4-4" stroke="#333" fill="none" stroke-width="1.3"/></svg>
    </div>
    <svg class="avatar" viewBox="0 0 30 30"><circle cx="15" cy="15" r="13.5" fill="none" stroke="#CC0000" stroke-width="2.5"/><circle cx="15" cy="11" r="5" fill="#CC0000"/><path d="M6 24c2-5 16-5 18 0" fill="#CC0000"/></svg>
    <svg class="abs" style="left:1057px;top:37px" width="10" height="6" viewBox="0 0 10 6"><path d="M1 1l4 4 4-4" stroke="#333" fill="none" stroke-width="1.3"/></svg>
  </header>

  <nav class="subnav">
    <span class="current">Search</span>
    <span style="left:520px">Leads</span>
    <span style="left:606px">Prospects</span>
    <span style="left:715px">Companies</span>
  </nav>
  <div class="crumbs"><span>People</span><span class="sep"></span><span>Daniel Harlow (477428)</span></div>

  <div class="back">
    <svg width="7" height="10" viewBox="0 0 7 10"><path d="M6 1L2 5l4 4" stroke="#333" fill="none" stroke-width="1.3"/></svg>Back List
  </div>
  <div class="pager" style="left:372px"><svg width="7" height="10" viewBox="0 0 7 10"><path d="M5 1L1.5 5 5 9" stroke="#333" fill="none" stroke-width="1.3"/></svg></div>
  <div class="pager" style="left:402px"><svg width="7" height="10" viewBox="0 0 7 10"><path d="M2 1l3.5 4L2 9" stroke="#333" fill="none" stroke-width="1.3"/></svg></div>

  <aside class="card">
    <div class="photo" role="img" aria-label="Customer portrait photo"></div>
    <div class="card-name">Daniel Harlow (477428)</div>
    <div class="send">Send Email
      <svg width="30" height="12" viewBox="0 0 30 12"><path d="M1 4h6M0 7h6M2 10h5" stroke="#fff"/><rect x="10" y="1" width="19" height="10" fill="none" stroke="#fff"/><path d="M10 1l9.5 6 9.5-6" stroke="#fff" fill="none"/></svg>
    </div>
    <ul class="facts">
      <li><span class="k">DOB</span>10/22/1965</li>
      <li><span class="k">Address</span>123 Street Road</li>
      <li><span class="k">Preferred Phone</span>(123) 456-7890</li>
      <li><span class="k">Preferred Contact</span>Phone</li>
      <li><span class="k">Email</span>info@harlowmail.com</li>
      <li><span class="k">Avg. Product Rating</span>
        <span class="stars">
          <svg width="14" height="14" viewBox="0 0 10 10"><path d="M5 0l1.5 3.3 3.5.4-2.6 2.4.7 3.5L5 7.8 1.9 9.6l.7-3.5L0 3.7l3.5-.4z" fill="#F5C518"/></svg>
          <svg width="14" height="14" viewBox="0 0 10 10"><path d="M5 0l1.5 3.3 3.5.4-2.6 2.4.7 3.5L5 7.8 1.9 9.6l.7-3.5L0 3.7l3.5-.4z" fill="#F5C518"/></svg>
          <svg width="14" height="14" viewBox="0 0 10 10"><path d="M5 0l1.5 3.3 3.5.4-2.6 2.4.7 3.5L5 7.8 1.9 9.6l.7-3.5L0 3.7l3.5-.4z" fill="#F5C518"/></svg>
          <svg width="14" height="14" viewBox="0 0 10 10"><path d="M5 0l1.5 3.3 3.5.4-2.6 2.4.7 3.5L5 7.8 1.9 9.6l.7-3.5L0 3.7l3.5-.4z" fill="#F5C518"/></svg>
          <svg width="14" height="14" viewBox="0 0 10 10"><path d="M5 .8l1.3 2.9 3 .4-2.2 2 .6 3L5 7.6 2.3 9.1l.6-3-2.2-2 3-.4z" fill="none" stroke="#F5C518" stroke-width=".8"/></svg>
        </span></li>
      <li><span class="k">Avg. Vendor Rating</span>
        <span class="stars">
          <svg width="14" height="14" viewBox="0 0 10 10"><path d="M5 0l1.5 3.3 3.5.4-2.6 2.4.7 3.5L5 7.8 1.9 9.6l.7-3.5L0 3.7l3.5-.4z" fill="#F5C518"/></svg>
          <svg width="14" height="14" viewBox="0 0 10 10"><path d="M5 0l1.5 3.3 3.5.4-2.6 2.4.7 3.5L5 7.8 1.9 9.6l.7-3.5L0 3.7l3.5-.4z" fill="#F5C518"/></svg>
          <svg width="14" height="14" viewBox="0 0 10 10"><path d="M5 0l1.5 3.3 3.5.4-2.6 2.4.7 3.5L5 7.8 1.9 9.6l.7-3.5L0 3.7l3.5-.4z" fill="#F5C518"/></svg>
          <svg width="14" height="14" viewBox="0 0 10 10"><path d="M5 0l1.5 3.3 3.5.4-2.6 2.4.7 3.5L5 7.8 1.9 9.6l.7-3.5L0 3.7l3.5-.4z" fill="#F5C518"/></svg>
          <svg width="14" height="14" viewBox="0 0 10 10"><path d="M5 .8l1.3 2.9 3 .4-2.2 2 .6 3L5 7.6 2.3 9.1l.6-3-2.2-2 3-.4z" fill="none" stroke="#F5C518" stroke-width=".8"/></svg>
        </span></li>
      <li><span class="k">Employer</span>N/A</li>
      <li><span class="k">Job Title</span>N/A</li>
      <li><span class="k">Assigned to</span>Rosa Lindqvist</li>
    </ul>
    <div class="updated">
      <div class="k">Last Updated<br>
        <svg width="18" height="18" viewBox="0 0 18 18" style="margin-top:4px"><path d="M3 8a6 6 0 0 1 11-3M15 10a6 6 0 0 1-11 3" stroke="#fff" fill="none" stroke-width="1.4"/><path d="M14 2v3h-3M4 16v-3h3" stroke="#fff" fill="none" stroke-width="1.4"/></svg>
      </div>
      <div>Dec 2, 2017<br>10.13 AM by<br>Peter Vance</div>
    </div>
  </aside>

  <nav class="tabs">
    <div class="tab" style="width:114px">
      <svg width="16" height="18" viewBox="0 0 16 18"><rect x=".5" y=".5" width="15" height="17" fill="none" stroke="#555"/><path d="M3 5h10M3 8h10M3 11h10M3 14h6" stroke="#555"/></svg>Summary</div>
    <div class="tab active" style="width:89px">
      <svg width="14" height="16" viewBox="0 0 14 16"><circle cx="7" cy="4.5" r="3.5" fill="none" stroke="#fff" stroke-width="1.3"/><path d="M1 16c0-5 12-5 12 0" fill="none" stroke="#fff" stroke-width="1.3"/></svg>Profile</div>
    <div class="tab" style="width:97px">
      <svg width="20" height="17" viewBox="0 0 20 17"><path d="M0 1h3l2.5 10h11l2-7H5" fill="none" stroke="#555" stroke-width="1.2"/><circle cx="7" cy="14.5" r="1.5" fill="none" stroke="#555"/><circle cx="15" cy="14.5" r="1.5" fill="none" stroke="#555"/></svg>Orders</div>
    <div class="tab" style="width:179px">
      <svg width="20" height="18" viewBox="0 0 20 18"><rect x="3" y="3" width="7" height="7" fill="none" stroke="#555" transform="rotate(20 6 6)"/><rect x="10" y="8" width="7" height="7" fill="none" stroke="#555" transform="rotate(-15 13 11)"/></svg>Tasks &amp; Interactions</div>
    <div class="tab" style="width:128px">
      <svg width="18" height="16" viewBox="0 0 18 16"><path d="M.5.5h17v11H6l-4 3.5v-3.5H.5z" fill="none" stroke="#555"/><path d="M4 4h10M4 7h10" stroke="#555"/></svg>Comments</div>
  </nav>
  <div class="tab-line"></div>
  <section class="panel"></section>

  <ul class="sections">
    <li class="active">Name &amp; Contact Info</li>
    <li>Vehicle Info</li>
    <li>Payment Methods</li>
    <li>Web Logins</li>
  </ul>

  <form class="form">
    <div class="field"><label>Prefix</label><div class="input"><span></span><svg width="7" height="4" viewBox="0 0 7 4"><path d="M.5.5l3 3 3-3" stroke="#555" fill="none"/></svg></div></div>
    <div class="field"><label>Suffix</label><div class="input"><span></span><svg width="7" height="4" viewBox="0 0 7 4"><path d="M.5.5l3 3 3-3" stroke="#555" fill="none"/></svg></div></div>
    <div class="field"><label>Age Range</label><div class="input"><span></span><svg width="7" height="4" viewBox="0 0 7 4"><path d="M.5.5l3 3 3-3" stroke="#555" fill="none"/></svg></div></div>
    <div class="field"><label>Gender</label><div class="seg"><span class="on">Male</span><span>Female</span></div></div>
    <div class="field"><label>First Name *</label><div class="input">Daniel</div></div>
    <div class="field"><label>Address 1 *</label><div class="input">123 Street Road</div></div>
    <div class="field"><label>Middle Initial</label><div class="input"></div></div>
    <div class="field"><label>Address 2</label><div class="input"></div></div>
    <div class="field"><label>Last Name *</label><div class="input">Harlow</div></div>
    <div class="field"><label>State/Province *</label><div class="input"><span></span><svg width="7" height="4" viewBox="0 0 7 4"><path d="M.5.5l3 3 3-3" stroke="#555" fill="none"/></svg></div></div>
    <div class="field"><label>Email Address</label><div class="input">info@harlowmail.com</div></div>
    <div class="field"><label>Zip/Postal Code *</label><div class="input"><span></span><svg width="7" height="4" viewBox="0 0 7 4"><path d="M.5.5l3 3 3-3" stroke="#555" fill="none"/></svg></div></div>
  </form>
  <div class="scroll"><i></i></div>

  <div class="save">Save Data
    <svg width="14" height="14" viewBox="0 0 14 14"><rect x=".5" y=".5" width="13" height="13" fill="none" stroke="#fff"/><rect x="3.5" y=".5" width="7" height="4" fill="none" stroke="#fff"/><path d="M3 8h8M3 10h8M3 12h8" stroke="#fff"/></svg>
  </div>
</div>
</body>
</html>
```